Hi, We're looking for a really attractive, professional brochure design for our FloraVan. The design will be used as a PDF for emailing & printed for trade shows - view www.floravan.com.au for product details

Envisage the brochure to be A4 size vertical format & contain 4-6 pages
In brief, it will have most of the information from our website, just in brouchere format

Target Market(s)

Middle age, retired couples with disposal income

Font styles to use
Sans Serif

Requirements
Must have
• Abality to add more pages later as new size product is released
Nice to have
• Would be nice for it to be innovative - like our product

```html
<!DOCTYPE html>
<html lang="en">
<head>
<meta charset="utf-8">
<title>FloraVan Tri-fold Brochure</title>
<link href="https://fonts.googleapis.com/css2?family=Lato:wght@400;700&display=swap" rel="stylesheet">
<style>
:root{
  --page:#e6ebec;
  --charcoal:#2e3436;
  --charcoal-soft:#4a5254;
  --teal:#2a6f8a;
  --teal-deep:#1d4f63;
  --sea:#1f5c70;
  --sea-light:#6a9fb0;
  --ink:#23302f;
  --ink-soft:#3b4a4f;
  --white:#ffffff;
  --sand:#c9b79a;
}
*{margin:0;padding:0;box-sizing:border-box}
html,body{width:800px;height:1200px;overflow:hidden;background:var(--page);font-family:"Lato",Arial,sans-serif}
.canvas{position:relative;width:800px;height:1200px;background:var(--page)}
.sheet{position:absolute;left:21px;width:758px;overflow:hidden;background:var(--white)}
.sheet--outer{top:18px;height:566px}
.sheet--inner{top:606px;height:576px}
.abs{position:absolute}
.photo{position:absolute}
/* outer sheet */
.panel-welcome{left:0;top:0;width:259px;height:566px;background:var(--charcoal);overflow:hidden}
.welcome-title{left:39px;top:48px;color:var(--white);font-size:17.5px;line-height:1.25}
.pricing-title{left:34px;top:296px;color:var(--white);font-size:14.4px;line-height:1.25;text-transform:uppercase}
.pricing-copy{left:32px;top:357px;width:196px;color:#e8eef0;font-size:8.2px;line-height:1.36}
.panel-services{left:259px;top:0;width:246px;height:566px;background:var(--white)}
.services-title{left:25px;top:60px;color:var(--white);font-size:17.6px;letter-spacing:.3px}
.service{position:absolute;left:20px;width:200px}
.service-icon{position:absolute;left:0;top:0}
.service h3{margin-left:44px;font-weight:400;font-size:12px;line-height:1.3;color:#cfe0e5}
.service p{margin-top:8px;font-size:7.8px;line-height:1.4;color:#e4eef1}
.panel-more{left:505px;top:0;width:253px;height:566px;overflow:hidden}
.more-title{left:46px;top:86px;color:var(--ink);font-size:15px;letter-spacing:.2px}
.more-list{left:30px;top:110px;width:215px;list-style:none}
.more-list li{position:relative;padding-left:16px;font-size:8px;line-height:1.35;color:var(--ink);height:29.5px}
.more-list svg{position:absolute;left:0;top:1px}
.call{left:106px;top:478px;color:var(--white);font-size:12.8px;line-height:1.32}
/* inner sheet */
.biz-tab{left:30px;top:0;width:211px;height:34px;background:var(--charcoal-soft)}
.biz-title{left:33px;top:82px;color:var(--white);font-size:24px;letter-spacing:.4px}
.biz-line{position:absolute;left:33px;color:#dfe5e6;font-size:8px;line-height:1.4}
.about-title{left:286px;top:36px;color:var(--ink);font-size:19.5px}
.about-sub{left:286px;top:60px;color:var(--ink);font-size:12px}
.about-copy{left:286px;top:86px;width:196px;color:var(--ink);font-size:8.2px;line-height:1.35}
.tagline-shore{left:45px;top:443px;color:var(--white);font-size:14.2px;line-height:1.27;text-transform:uppercase}
.brand{left:553px;top:43px;display:flex;align-items:center;gap:9px;color:var(--white)}
.brand-mark{width:30px;height:30px;border:3px solid var(--white)}
.brand-name{font-size:17.5px;line-height:1}
.brand-tag{font-size:7.2px;letter-spacing:.5px;margin-top:5px}
.holiday-box{left:554px;top:474px;width:204px;height:84px;background:var(--teal);color:var(--white);font-size:12px;line-height:1.3;padding:14px 0 0 27px;text-transform:uppercase}
</style>
</head>
<body>
<div class="canvas">

  <section class="sheet sheet--outer">
    <div class="abs panel-welcome">
      <svg class="photo" width="259" height="566" viewBox="0 0 259 566" role="img" aria-label="Photo of a white FloraVan cruising through open water with spray">
        <defs>
          <linearGradient id="seaA" x1="0" y1="0" x2="0" y2="1">
            <stop offset="0" stop-color="#4a6f86"/><stop offset=".5" stop-color="#2f5673"/><stop offset="1" stop-color="#274a63"/>
          </linearGradient>
        </defs>
        <path d="M0 236 C60 200 120 260 190 240 C225 230 245 222 259 224 L259 566 L0 566 Z" fill="url(#seaA)"/>
      </svg>
      <svg class="photo" style="left:56px;top:132px" width="138" height="138" viewBox="0 0 138 138" role="img" aria-label="Photo of the wheelhouse interior with timber cabinetry">
        <defs><linearGradient id="cabin" x1="0" y1="0" x2="1" y2="1"><stop offset="0" stop-color="#c7cfd6"/><stop offset=".45" stop-color="#c8702e"/><stop offset="1" stop-color="#e9e3d6"/></linearGradient></defs>
        <circle cx="69" cy="69" r="66" fill="url(#cabin)" stroke="#b9d9e1" stroke-width="4"/>
      </svg>
      <h1 class="abs welcome-title" style="font-weight:400">Welcome to<br>Our Company...</h1>
      <h2 class="abs pricing-title" style="font-weight:400">FloraVan<br>Pricing<br>&amp; Specifications</h2>
      <p class="abs pricing-copy">Lorem ipsum dolor sit amet, consectetur adipisice elit, sed do eiusmod tempor incididunt ut labor et dolore magna aliqua. Ut enim ad minim venia quis nostrud exercitation ullamco laboris nisi ut aliquip elcommodo consequat. Duis aute ir reprehenderit in voluptate velit esse cillum dolore eu fu pariatur. Excepteur sint occaecat cupidatat non proid sunt in culpa qui officia deserunt mollit anim i laborum. Sed ut perspiciatis unde omnis iste ar voluptatem accusantium doloremque laudantium, to aperiam, eaque ipsa quae ab illo inventore verita architecto beatae vitae dicta sunt explicabo. Nemo en ipsam voluptatem quia voluptas sit.</p>
    </div>

    <div class="abs panel-services">
      <svg class="photo" style="left:8px;top:14px" width="230" height="528" viewBox="0 0 230 528" role="img" aria-label="Photo of deep teal sea water breaking into white surf">
        <defs>
          <linearGradient id="surf" x1="0" y1="0" x2="0" y2="1">
            <stop offset="0" stop-color="#1f5a6e"/><stop offset=".55" stop-color="#2e7486"/><stop offset=".8" stop-color="#8fb9c4"/><stop offset="1" stop-color="#f4f8f9"/>
          </linearGradient>
        </defs>
        <rect width="230" height="528" fill="url(#surf)"/>
      </svg>
      <h2 class="abs services-title" style="font-weight:400">OUR SERVICES</h2>

      <div class="service" style="top:122px">
        <svg class="service-icon" width="30" height="30" viewBox="0 0 30 30"><polygon points="15,1 28,8 28,22 15,29 2,22 2,8" fill="#3d4446"/><circle cx="15" cy="15" r="6" fill="none" stroke="#cfd6d8" stroke-width="1.2"/><path d="M12 15l2 2 4-4" fill="none" stroke="#cfd6d8" stroke-width="1.2"/></svg>
        <h3>Panoramic<br>Viewing</h3>
        <p>The FloraVan features large windows, offering great ventilation and an amazing view. You still have complete privacy when required with the Roman Blind style window treatments.</p>
      </div>
      <div class="service" style="top:216px">
        <svg class="service-icon" width="30" height="30" viewBox="0 0 30 30"><polygon points="15,1 28,8 28,22 15,29 2,22 2,8" fill="#3d4446"/><circle cx="15" cy="15" r="6" fill="none" stroke="#cfd6d8" stroke-width="1.2"/><path d="M12 15l2 2 4-4" fill="none" stroke="#cfd6d8" stroke-width="1.2"/></svg>
        <h3>Shallow<br>Draft</h3>
        <p>Let out your inner explorer, the FloraVan's shallow draft enables you to access many rivers and great camping spots. This also allows access to ankle deep water when going ashore, so</p>
      </div>
      <div class="service" style="top:310px">
        <svg class="service-icon" width="30" height="30" viewBox="0 0 30 30"><polygon points="15,1 28,8 28,22 15,29 2,22 2,8" fill="#3d4446"/><circle cx="15" cy="15" r="6" fill="none" stroke="#cfd6d8" stroke-width="1.2"/><path d="M12 15l2 2 4-4" fill="none" stroke="#cfd6d8" stroke-width="1.2"/></svg>
        <h3>Full Height<br>Pantry</h3>
        <p>Great for travel over longer periods, the FloraVan's full height pantry enables you to stock up for that long trip without the need to stop for more supplies. All food is in the one place, and there's no poking around small lockers.</p>
      </div>
      <div class="service" style="top:411px">
        <svg class="service-icon" width="30" height="30" viewBox="0 0 30 30"><polygon points="15,1 28,8 28,22 15,29 2,22 2,8" fill="#3d4446"/><circle cx="15" cy="15" r="6" fill="none" stroke="#cfd6d8" stroke-width="1.2"/><path d="M12 15l2 2 4-4" fill="none" stroke="#cfd6d8" stroke-width="1.2"/></svg>
        <h3 style="color:#1d3c47">Reduced Height<br>On Trailer</h3>
        <p style="color:var(--ink)">The FloraVan's wheel arches are set into the hull reducing the overall height which allows for easier access, reduced fuel consumption and an overall aesthetically pleasing look.</p>
      </div>
    </div>

    <div class="abs panel-more">
      <svg class="photo" width="253" height="566" viewBox="0 0 253 566" role="img" aria-label="Photos of the cabin helm with cream seating, and the FloraVan moored at sunset">
        <defs>
          <linearGradient id="helm" x1="0" y1="0" x2="1" y2="1"><stop offset="0" stop-color="#b7ada0"/><stop offset=".5" stop-color="#d8cfc0"/><stop offset="1" stop-color="#a9957a"/></linearGradient>
          <linearGradient id="dusk" x1="0" y1="0" x2="0" y2="1"><stop offset="0" stop-color="#c9c2ae"/><stop offset=".45" stop-color="#6d7b7e"/><stop offset="1" stop-color="#2b3a44"/></linearGradient>
        </defs>
        <rect width="253" height="566" fill="url(#helm)"/>
        <rect width="253" height="566" fill="#ffffff" opacity=".35"/>
        <path d="M0 370 C70 330 150 400 253 345 L253 566 L0 566 Z" fill="#ffffff"/>
        <path d="M0 382 C70 345 150 412 253 360 L253 566 L0 566 Z" fill="url(#dusk)"/>
      </svg>
      <svg class="photo" style="left:60px;top:284px" width="116" height="116" viewBox="0 0 116 116" role="img" aria-label="Photo of the pantry with timber doors and blue lighting">
        <defs><linearGradient id="pantry" x1="0" y1="0" x2="1" y2="0"><stop offset="0" stop-color="#4d5fb0"/><stop offset=".5" stop-color="#c5d3ea"/><stop offset="1" stop-color="#c7702e"/></linearGradient></defs>
        <circle cx="58" cy="58" r="55" fill="url(#pantry)" stroke="#b9d9e1" stroke-width="4"/>
      </svg>
      <h2 class="abs more-title" style="font-weight:700">MORE SERVICES</h2>
      <ul class="abs more-list" style="top:112px">
        <li><svg width="12" height="12" viewBox="0 0 12 12"><circle cx="6" cy="6" r="5.2" fill="none" stroke="#23302f" stroke-width="1.1"/><path d="M3.6 6.1l1.7 1.7 3.2-3.3" fill="none" stroke="#23302f" stroke-width="1.1"/></svg>Full Fibreglass Composite Construction. No Aluminium or Steel to Corrode or rust.</li>
        <li><svg width="12" height="12" viewBox="0 0 12 12"><circle cx="6" cy="6" r="5.2" fill="none" stroke="#23302f" stroke-width="1.1"/><path d="M3.6 6.1l1.7 1.7 3.2-3.3" fill="none" stroke="#23302f" stroke-width="1.1"/></svg>Sleek, aerodynamic shape with the latest modern styling</li>
        <li><svg width="12" height="12" viewBox="0 0 12 12"><circle cx="6" cy="6" r="5.2" fill="none" stroke="#23302f" stroke-width="1.1"/><path d="M3.6 6.1l1.7 1.7 3.2-3.3" fill="none" stroke="#23302f" stroke-width="1.1"/></svg>Stylish modern fit out with choice of varnished timbers &amp; veneers.</li>
        <li><svg width="12" height="12" viewBox="0 0 12 12"><circle cx="6" cy="6" r="5.2" fill="none" stroke="#23302f" stroke-width="1.1"/><path d="M3.6 6.1l1.7 1.7 3.2-3.3" fill="none" stroke="#23302f" stroke-width="1.1"/></svg>Together with a abundance of counter top space &amp; storage.</li>
        <li><svg width="12" height="12" viewBox="0 0 12 12"><circle cx="6" cy="6" r="5.2" fill="none" stroke="#23302f" stroke-width="1.1"/><path d="M3.6 6.1l1.7 1.7 3.2-3.3" fill="none" stroke="#23302f" stroke-width="1.1"/></svg>The throttle box folds away when not required, offering more room.</li>
      </ul>
      <p class="abs call">Call Us<br>+61 2 5550 1842<br>+61 2 5550 7391</p>
    </div>
  </section>

  <section class="sheet sheet--inner">
    <div class="abs biz-tab"></div>
    <svg class="photo" style="left:0;top:0" width="506" height="576" viewBox="0 0 506 576">
      <path d="M14 34 L259 34 L259 300 C200 292 150 318 100 335 C70 345 40 350 14 344 Z" fill="var(--charcoal)"/>
    </svg>
    <svg class="photo" style="left:0;top:0" width="506" height="576" viewBox="0 0 506 576" role="img" aria-label="Photo of the FloraVan beached on a sandy shore with two people wading nearby">
      <defs>
        <linearGradient id="shore" x1="0" y1="0" x2="0" y2="1">
          <stop offset="0" stop-color="#3f6b4c"/><stop offset=".3" stop-color="#8fa6a0"/><stop offset=".45" stop-color="#d8d4c6"/><stop offset=".6" stop-color="#3c6f8c"/><stop offset="1" stop-color="#23455e"/>
        </linearGradient>
      </defs>
      <path d="M0 408 C90 396 190 382 280 378 C370 374 440 356 506 352 L506 576 L0 576 Z" fill="url(#shore)"/>
    </svg>
    <h2 class="abs biz-title" style="font-weight:700">BUSINESS</h2>
    <svg class="abs" style="left:33px;top:123px" width="16" height="16" viewBox="0 0 16 16"><circle cx="8" cy="8" r="7" fill="none" stroke="#fff" stroke-width="1"/><ellipse cx="8" cy="8" rx="3" ry="7" fill="none" stroke="#fff" stroke-width="1"/><path d="M1 8h14M2.5 4.5h11M2.5 11.5h11" stroke="#fff" stroke-width=".9"/></svg>
    <p class="biz-line" style="top:146px">Email : hello@floravan.com.au<br>Web : www.floravan.com.au</p>
    <svg class="abs" style="left:34px;top:186px" width="12" height="16" viewBox="0 0 12 16"><path d="M6 1a5 5 0 0 1 5 5c0 4-5 9-5 9S1 10 1 6a5 5 0 0 1 5-5z" fill="#fff"/><circle cx="6" cy="6" r="2" fill="var(--charcoal)"/></svg>
    <p class="biz-line" style="top:207px">Add : 7112 Your Adderss gos here<br>Street 123, Country.</p>
    <svg class="abs" style="left:34px;top:244px" width="12" height="16" viewBox="0 0 12 16"><path d="M6 1a5 5 0 0 1 5 5c0 4-5 9-5 9S1 10 1 6a5 5 0 0 1 5-5z" fill="#fff"/><circle cx="6" cy="6" r="2" fill="var(--charcoal)"/></svg>
    <p class="biz-line" style="top:265px">Add : 7112 Your Adderss gos here<br>Street 123, Country.</p>

    <h2 class="abs about-title" style="font-weight:700">ABOUT US</h2>
    <p class="abs about-sub">something about us</p>
    <p class="abs about-copy">The FloraVan boasts some amazing fixtures and features many of which are standard equipment. Models can have a "hidden helm" which when in caravan mode the boat steering and engine controls are not required, conveniently disappear into a cupboard. Twin engine design not only is a great safety feature but also makes for easy control and maneuverability, standard equipment is for two, 30 hp, fuel injected four stroke outboards, which combined put around 30 amps back into the batteries and are easily pull-started if required. Top speed is around 17 knots and a very economical cruise speed is around 13-15 knots.The FloraVan draws a mere 200 mm at rest which allows it to be easily nudged against river banks or sneak into very shallow anchorages. FloraVan is easily launched and recovered thanks to a purpose built trailer. 4 wheel disc brakes and a break away safety system are standard equipment. 200 litre water tanks and up to 80 litres of fuel allows for lengthy cruising. A grey water tank can also be included for those environmentally sensitive waterways or when</p>

    <p class="abs tagline-shore">FloraVan is<br>the best<br>solution<br>for sea<br>travels.</p>

    <svg class="photo" style="left:506px;top:0" width="252" height="576" viewBox="0 0 252 576" role="img" aria-label="Photo of the FloraVan bow on the water in front of a tree-lined bank">
      <defs>
        <linearGradient id="bow" x1="0" y1="0" x2="0" y2="1">
          <stop offset="0" stop-color="#dfe9ee"/><stop offset=".25" stop-color="#5d7a4e"/><stop offset=".4" stop-color="#e9eef1"/><stop offset=".7" stop-color="#6f95b0"/><stop offset="1" stop-color="#3a6a8c"/>
        </linearGradient>
      </defs>
      <rect width="252" height="576" fill="url(#bow)"/>
      <path d="M0 0 H252 V140 C190 120 130 160 70 150 C40 145 15 138 0 142 Z" fill="var(--teal)"/>
      <path d="M0 142 C15 138 40 145 70 150 C130 160 190 120 252 140 V146 C190 128 130 168 70 158 C40 153 15 146 0 150 Z" fill="#ffffff"/>
    </svg>
    <div class="abs brand">
      <span class="brand-mark"></span>
      <div>
        <div class="brand-name">Marketing</div>
        <div class="brand-tag">TAGLINE GOSE HERE</div>
      </div>
    </div>
    <div class="abs holiday-box">Enjoy your<br>holidays<br>with<br>best FloraVans,</div>
  </section>

</div>
</body>
</html>
```